Breakfast Cafe - The Sunny Perch

It is for my breakfast and lunch cafe with a hawaiian / beach theme. I am open 7 days a week from 7am to 2pm. We serve traditional American food such as omelettes, pancakes, burgers and sandwiches. I'll upload my old card and my new logo to be used. We have a lot of day to day regulars who eat there during the week, our t-shirts actually say 'Locals Only' on them. Hope this helps. Thanks.

Target Market(s)

anyone who has an appetite!

Industry/Entity Type

American Restaurant

Contact Information for Business Card

7340D Marlin Harbor Road
Long Beach, California
(555) 317-2286

Requirements
Must have
• Address and phone number easily readable.
Nice to have
• beach or tropical theme

```html
<!DOCTYPE html>
<html lang="en">
<head>
<meta charset="utf-8">
<title>The Sunny Perch – Business Card</title>
<link rel="stylesheet" href="https://fonts.googleapis.com/css2?family=Bree+Serif&display=swap">
<style>
  :root {
    --wood-light: #b8662a;
    --wood-mid: #a0531d;
    --wood-dark: #7e3f14;
    --paper: #ffffff;
    --gold: #f0c77e;
    --cream: #fff3dc;
    --panel: rgba(255, 236, 200, 0.12);
    --brand-orange: #e08a2c;
    --brand-teal: #2a9fb0;
    --brand-brown: #6b3a16;
  }
  * { margin: 0; padding: 0; box-sizing: border-box; }
  html, body { width: 681px; height: 1200px; overflow: hidden; }
  body { font-family: "Bree Serif", Georgia, serif; }

  .card {
    position: relative;
    width: 681px;
    height: 1200px;
    background: linear-gradient(100deg, var(--wood-mid) 0%, var(--wood-light) 35%, var(--wood-mid) 60%, var(--wood-light) 85%, var(--wood-dark) 100%);
    overflow: hidden;
  }
  .card-header {
    position: absolute;
    inset: 0 0 auto 0;
    height: 430px;
  }
  .card-header svg { display: block; width: 100%; height: 100%; }

  .brand {
    position: absolute;
    top: 40px;
    left: 0;
    right: 0;
    display: flex;
    flex-direction: column;
    align-items: center;
    gap: 22px;
  }
  .brand-mark {
    width: 230px;
    height: 230px;
    border-radius: 50%;
    background: radial-gradient(circle at 50% 40%, #f7c56a 0%, var(--brand-orange) 55%, #b7621f 100%);
  }
  .brand-name {
    font-size: 52px;
    color: var(--brand-teal);
    letter-spacing: 1px;
  }

  .info {
    position: absolute;
    left: 0;
    right: 0;
    top: 500px;
    display: flex;
    flex-direction: column;
    align-items: center;
    gap: 74px;
  }
  .info-box {
    position: relative;
    border: 3px solid var(--gold);
    border-radius: 10px;
    background: var(--panel);
    color: var(--cream);
    text-align: center;
    padding: 26px 34px 20px;
    font-size: 34px;
    line-height: 1.25;
  }
  .info-box.hours { width: 330px; }
  .info-box.address { width: 470px; font-size: 31px; }
  .info-box.phone { width: 280px; padding: 20px 20px 14px; font-size: 36px; }
  .info-icon {
    position: absolute;
    top: -24px;
    left: 50%;
    transform: translateX(-50%);
    width: 44px;
    height: 44px;
    border-radius: 50%;
    background: var(--wood-mid);
    display: flex;
    align-items: center;
    justify-content: center;
  }
  .info-icon svg { width: 30px; height: 30px; }
</style>
</head>
<body>
  <main class="card">
    <header class="card-header">
      <svg viewBox="0 0 681 430" preserveAspectRatio="none" aria-hidden="true">
        <path d="M0 0 H681 V300 Q340.5 470 0 300 Z" fill="var(--paper)"/>
      </svg>
      <div class="brand">
        <div class="brand-mark" role="img" aria-label="Round brand emblem with a tropical beach scene"></div>
        <div class="brand-name">The Sunny Perch</div>
      </div>
    </header>

    <section class="info">
      <div class="info-box hours">
        <span class="info-icon">
          <svg viewBox="0 0 24 24" fill="none" stroke="var(--gold)" stroke-width="2" stroke-linecap="round">
            <path d="M7 3v8M5 3v4a2 2 0 0 0 4 0V3M7 11v10"/>
            <path d="M17 3c-2 2-2 6 0 8v10"/>
          </svg>
        </span>
        Breakfast &amp; Lunch<br>7am – 2pm Daily
      </div>

      <div class="info-box address">
        <span class="info-icon">
          <svg viewBox="0 0 24 24" fill="var(--gold)">
            <path d="M12 2a7 7 0 0 0-7 7c0 5 7 13 7 13s7-8 7-13a7 7 0 0 0-7-7zm0 9.5A2.5 2.5 0 1 1 12 6.5a2.5 2.5 0 0 1 0 5z"/>
          </svg>
        </span>
        7340D Marlin Harbor Road<br>Long Beach, California 90899
      </div>

      <div class="info-box phone">
        <span class="info-icon">
          <svg viewBox="0 0 24 24" fill="var(--gold)">
            <path d="M6.6 10.8a15.1 15.1 0 0 0 6.6 6.6l2.2-2.2a1 1 0 0 1 1-.25 11.4 11.4 0 0 0 3.6.57 1 1 0 0 1 1 1V20a1 1 0 0 1-1 1A17 17 0 0 1 3 4a1 1 0 0 1 1-1h3.5a1 1 0 0 1 1 1c0 1.25.2 2.45.57 3.57a1 1 0 0 1-.25 1z"/>
          </svg>
        </span>
        (555) 317-2286
      </div>
    </section>
  </main>
</body>
</html>
```